Redesign Login page

I want to redesign my login page to bring my 2 products closer together. I am only looking to redesign one login page, not 2.

For the logo, please make it solid and it can be black or white if helpful. I can also fine tune the logo if you get it close.

Coding

Coded - Design and coding required

Number of Pages Required

1 page

```html
<!DOCTYPE html>
<html lang="en">
<head>
<meta charset="UTF-8">
<title>Lumora – Login</title>
<link href="https://fonts.googleapis.com/css2?family=Poppins:wght@400;500;600;700&display=swap" rel="stylesheet">
<style>
  :root {
    --page-bg: #ffffff;
    --card-bg: #ffffff;
    --card-border: #e4e4e4;
    --field-border: #d9d9d9;
    --text-main: #2b2b2b;
    --text-muted: #6b6b6b;
    --placeholder: #8a8a8a;
    --brand: #a03020;
    --divider: #cfcfcf;
    --toggle-bg: #ececec;
    --icon-grey: #b5b5b5;
    --social-border: #e6e6e6;
  }
  * { box-sizing: border-box; margin: 0; padding: 0; }
  html, body {
    width: 1200px; height: 905px; overflow: hidden;
    background: var(--page-bg);
    font-family: "Poppins", sans-serif;
  }
  .login-card {
    position: absolute; left: 268px; top: 90px;
    width: 676px; height: 737px;
    background: var(--card-bg);
    border: 1px solid var(--card-border);
    border-radius: 46px;
    box-shadow: 0 10px 50px rgba(0,0,0,0.06);
  }
  .brand-name {
    position: absolute; left: 0; right: 0; top: 58px;
    display: flex; justify-content: center; align-items: center; gap: 12px;
    font-size: 62px; font-weight: 700; color: var(--brand); letter-spacing: -1px;
    line-height: 1;
  }
  .brand-dot { width: 22px; height: 22px; border-radius: 50%; background: var(--brand); }
  .field {
    position: absolute; left: 57px; width: 570px; height: 77px;
    border: 1px solid var(--field-border); border-radius: 40px;
    box-shadow: 0 3px 6px rgba(0,0,0,0.08);
    display: flex; align-items: center; padding: 0 32px;
    background: #fff;
  }
  .field-email { top: 184px; }
  .field-password { top: 283px; }
  .field-icon { width: 22px; height: 22px; flex: none; }
  .field-sep { width: 1px; height: 30px; background: var(--field-border); margin: 0 12px 0 10px; }
  .field-label { font-size: 16px; color: var(--placeholder); flex: 1; }
  .field-toggle { width: 28px; height: 28px; flex: none; }
  .login-button {
    position: absolute; left: 57px; top: 383px; width: 570px; height: 78px;
    border-radius: 40px; background: var(--brand); color: #fff;
    font-size: 23px; font-weight: 500; display: flex; align-items: center; justify-content: center;
  }
  .remember {
    position: absolute; left: 57px; top: 477px;
    display: flex; align-items: center; gap: 14px;
    font-size: 17px; color: var(--text-muted);
  }
  .switch {
    width: 42px; height: 21px; border-radius: 11px; background: var(--toggle-bg);
    border: 1px solid #dcdcdc; position: relative;
  }
  .switch::after {
    content: ""; position: absolute; left: 1px; top: 1px;
    width: 17px; height: 17px; border-radius: 50%; background: #fff;
    box-shadow: 0 1px 2px rgba(0,0,0,0.2);
  }
  .forgot-link {
    position: absolute; right: 57px; top: 475px;
    font-size: 17px; color: var(--brand); text-decoration: underline;
  }
  .signup-line {
    position: absolute; left: 0; right: 0; top: 527px; text-align: center;
    font-size: 17px; color: var(--text-muted);
  }
  .signup-line a { color: var(--brand); text-decoration: underline; }
  .divider {
    position: absolute; left: 78px; right: 78px; top: 566px;
    display: flex; align-items: center; gap: 24px;
    font-size: 17px; font-weight: 500; color: var(--text-main);
  }
  .divider::before, .divider::after { content: ""; flex: 1; height: 1px; background: var(--divider); }
  .social-row {
    position: absolute; left: 0; right: 0; top: 615px;
    display: flex; justify-content: center; gap: 11px;
  }
  .social-button {
    width: 62px; height: 62px; border-radius: 50%;
    border: 1px solid var(--social-border); background: #fff;
    display: flex; align-items: center; justify-content: center;
  }
  .social-button span { width: 22px; height: 22px; border-radius: 50%; background: #d8d8d8; }
</style>
</head>
<body>
  <main class="login-card">
    <div class="brand-name"><span class="brand-dot"></span>Lumora</div>

    <div class="field field-email">
      <svg class="field-icon" viewBox="0 0 24 24" fill="none" stroke="#222" stroke-width="1.7"><circle cx="12" cy="8" r="4"/><path d="M4 21c0-4.4 3.6-7 8-7s8 2.6 8 7"/></svg>
      <span class="field-sep"></span>
      <span class="field-label">Email</span>
    </div>

    <div class="field field-password">
      <svg class="field-icon" viewBox="0 0 24 24" fill="none" stroke="#222" stroke-width="1.8"><rect x="4" y="10" width="16" height="11" rx="1"/><path d="M8 10V7a4 4 0 0 1 8 0v3"/><circle cx="12" cy="15" r="1.4" fill="#222"/></svg>
      <span class="field-sep"></span>
      <span class="field-label">Password</span>
      <svg class="field-toggle" viewBox="0 0 24 24" fill="none" stroke="var(--icon-grey)" stroke-width="1.6"><path d="M2 12s3.6-6 10-6 10 6 10 6-3.6 6-10 6S2 12 2 12z"/><circle cx="12" cy="12" r="3"/><path d="M4 20L20 4"/></svg>
    </div>

    <div class="login-button">LOGIN</div>

    <div class="remember"><span class="switch"></span>Remember Me</div>
    <a class="forgot-link">Forgot Password?</a>

    <p class="signup-line">Don't Have An Account? <a>Sign Up</a></p>

    <div class="divider">Or Sign In With</div>

    <div class="social-row">
      <div class="social-button"><span></span></div>
      <div class="social-button"><span></span></div>
      <div class="social-button"><span></span></div>
      <div class="social-button"><span></span></div>
    </div>
  </main>
</body>
</html>
```